Wattlegrove Aged Care Centre

We need a website design for an aged care facility in Brisbane (a different one to project already posted) with final design provided as a .psd file.

This website will be built on Dot Net Nuke so design needs to be able to be converted into a DNN skin and containers.

Target Market(s)

• Credibility
• Family orientated
• Establish an online identity
• Download a booking form for tours
• Receive general enquiries
• Feature a phone number
• Advertise career opportunities

Number of Pages Required

1 page

Requirements
Must have
• o The following elements are to be included in the design concepts:
• o Phone number will be featured in banner 07 3821 4476
• o Logo and words Marstow Care Centre to be featured in banner
• o Area for a flash banner of rotating images on homepage (have attached some images)
• o 3 x buttons to be designed and feature on homepage - Book a Tour, Contact Us and Sign up to our newsletter
• o No colour preference but perhaps keeping with their logo/branding but am open to ideas

```html
<!DOCTYPE html>
<html lang="en">
<head>
<meta charset="utf-8">
<title>Marstow Care Centre</title>
<link href="https://fonts.googleapis.com/css2?family=Tinos:wght@400;700&display=swap" rel="stylesheet">
<style>
  :root {
    --forest: #1e5511;
    --forest-deep: #17430d;
    --paper: #ffffff;
    --ink: #111111;
    --photo-sky: #e9ece6;
    --photo-stone: #b79a7c;
    --photo-leaf: #4f6b33;
    --photo-wood: #8a5b2e;
    --photo-wall: #d8d2c2;
  }
  * { margin: 0; padding: 0; box-sizing: border-box; }
  html, body { width: 1200px; height: 960px; overflow: hidden; }
  body {
    background: var(--forest);
    font-family: "Tinos", "Times New Roman", serif;
    color: var(--ink);
    position: relative;
  }
  .hero {
    position: absolute; left: 72px; top: 86px; width: 755px; height: 348px;
    background: linear-gradient(180deg, var(--photo-sky) 0%, var(--photo-wall) 30%, var(--photo-wood) 55%, var(--photo-leaf) 72%, var(--photo-stone) 86%, #9fa0a2 100%);
  }
  .hero-phone {
    position: absolute; left: 0; right: 0; top: 12px; text-align: center;
    font-size: 26px; color: var(--ink); padding-left: 140px;
  }
  .hero-title {
    position: absolute; left: 298px; bottom: 0; font-size: 44px; line-height: 1.2;
    color: var(--paper);
  }
  .brand {
    position: absolute; left: 834px; top: 98px; width: 328px; height: 328px;
    border-radius: 50%; background: var(--paper); border: 6px solid var(--forest-deep);
    display: flex; align-items: center; justify-content: center; text-align: center;
    color: var(--forest); font-size: 36px; line-height: 1.15; padding: 40px;
  }
  .nav {
    position: absolute; left: 72px; top: 434px; width: 1078px; height: 48px;
    background: var(--paper); display: flex; list-style: none;
  }
  .nav li {
    font-size: 34px; line-height: 48px; height: 48px; color: var(--ink);
  }
  .nav .home { width: 152px; padding-left: 24px; }
  .nav .about { width: 212px; background: var(--forest); color: var(--paper); text-align: center; }
  .nav .facilities { width: 172px; padding-left: 17px; }
  .nav .tours { width: 130px; padding-left: 2px; }
  .nav .careers { width: 162px; padding-left: 10px; }
  .nav .contact { padding-left: 14px; }
  .content {
    position: absolute; left: 72px; top: 496px; width: 949px; height: 340px;
    background: var(--paper); border-bottom-left-radius: 12px;
  }
  .flash-label { position: absolute; left: 14px; top: 14px; font-size: 26px; }
  .flash-area {
    position: absolute; left: 0; top: 55px; width: 186px; height: 276px;
    background: linear-gradient(180deg, #e6e1d6 0%, #c9b79a 30%, #a9753f 55%, #d9d6d0 68%, #6e4420 100%);
  }
  .welcome { position: absolute; left: 222px; top: 22px; width: 705px; font-size: 21.6px; line-height: 30px; }
  .copyright { position: absolute; left: 0; right: 0; bottom: 14px; text-align: center; font-size: 19px; padding-left: 160px; }
  .actions {
    position: absolute; left: 1036px; top: 496px; width: 114px; height: 340px;
    background: var(--paper); border-bottom-right-radius: 12px; list-style: none;
  }
  .action {
    position: absolute; left: 0; width: 114px; text-align: center;
    color: var(--forest); font-size: 18px; line-height: 24px;
  }
  .action svg { display: block; margin: 0 auto 2px; }
  .action-newsletter { top: 30px; }
  .action-contact { top: 130px; }
  .action-tour { top: 234px; }
</style>
</head>
<body>
  <header class="hero" role="img" aria-label="Photo of the care centre's covered entrance with columns and garden">
    <p class="hero-phone">Call Now On: 07 3821 4476</p>
    <h1 class="hero-title" style="font-weight:400">Marstow Care Centre</h1>
  </header>

  <div class="brand">Marstow Care Centre</div>

  <ul class="nav">
    <li class="home">Home</li>
    <li class="about">About Us</li>
    <li class="facilities">Facilities</li>
    <li class="tours">Tours</li>
    <li class="careers">Careers</li>
    <li class="contact">Contact Us</li>
  </ul>

  <main class="content">
    <p class="flash-label">Flash Banner</p>
    <div class="flash-area" role="img" aria-label="Rotating photo banner showing the centre's kitchen and servery"></div>
    <div class="welcome">
      <p>Welcome</p>
      <p>Lorem ipsum dolor sit amet, consectetur adipisicing elit, sed do eiusmod tempor incididunt ut labore et dolore magna aliqua. Ut enim ad minim veniam, quis nostrud exercitation ullamco laboris nisi ut aliquip ex ea commodo consequat. Duis aute irure dolor in reprehenderit in voluptate velit esse cillum dolore eu fugiat nulla pariatur. Excepteur sint occaecat cupidatat non proident, sunt in culpa qui officia deserunt mollit anim id est laborum</p>
    </div>
    <p class="copyright">© Marstow Care Centre 2009</p>
  </main>

  <ul class="actions">
    <li class="action action-newsletter">
      <svg width="74" height="34" viewBox="0 0 74 34" aria-hidden="true">
        <rect x="1" y="1" width="72" height="32" fill="var(--forest)"/>
        <path d="M1 1 L37 22 L73 1" fill="none" stroke="#fff" stroke-width="2"/>
        <path d="M1 33 L28 16 M73 33 L46 16" fill="none" stroke="#fff" stroke-width="1.5"/>
      </svg>
      Newsletter<br>Signup
    </li>
    <li class="action action-contact">
      <svg width="72" height="52" viewBox="0 0 72 52" aria-hidden="true">
        <path d="M4 16 Q4 4 36 4 Q68 4 68 16 L68 20 L54 20 L54 13 L18 13 L18 20 L4 20 Z" fill="var(--forest)"/>
        <path d="M14 24 L58 24 L66 50 L6 50 Z" fill="var(--forest)"/>
        <circle cx="36" cy="36" r="9" fill="#fff"/>
        <circle cx="36" cy="36" r="4" fill="var(--forest)"/>
      </svg>
      Contact<br>Us
    </li>
    <li class="action action-tour">
      <svg width="60" height="36" viewBox="0 0 60 36" aria-hidden="true">
        <path d="M4 4 L10 2 L44 26 L40 32 Z" fill="var(--forest)"/>
        <path d="M40 32 L44 26 L48 34 Z" fill="var(--forest)"/>
        <line x1="20" y1="34" x2="56" y2="34" stroke="var(--forest)" stroke-width="2"/>
      </svg>
      Book A<br>Tour
    </li>
  </ul>
</body>
</html>
```